Harbor Sushi & Steak Dinner Menu

I'm looking for a MENU design with a particular feel. I want to have a base template made that I can then use for future alterations to the menu; ie I can go in and change out different entrees as the menu changes but the template will remain the same. (Ideally it would be in an Apple Pages format.). Also ideally - dinner menu will occupy 2 pages 8.5 x 11. The restaurant's name is Harbor. It is a MODERN steak house that will also feature Sushi, a Raw Bar, Exquisite Cocktails and a sophisticated nightlife crowd. I have attached our LOGO, a secondary logo that we will be featuring throughout the project including on the menu cover (the gold U). Finally - I have attached the content that we would like to see. AGAIN - I REITERATE: High end dining and lounge atmosphere. A couple of restaurants / menus that I love are Morvendel in NYC and Pellucid Steakhouse in Long Island NY. Please do not duplicate - just trying to offer some suggestions.

Requirements
Must have
• A sophisticated and elegant feel without being stuffy or old.

```html
<!DOCTYPE html>
<html lang="en">
<head>
<meta charset="utf-8">
<title>Harbor Sushi &amp; Steak — Dinner Menu</title>
<link rel="stylesheet" href="https://fonts.googleapis.com/css2?family=Libre+Caslon+Text:ital,wght@0,400;0,700;1,700&family=Josefin+Sans:wght@400&display=swap">
<style>
  :root {
    --ink-bg: #050505;
    --ink-bg-glow: #1c1c1c;
    --gold-text: #e9d08e;
    --gold-logo: #d8bf7c;
    --band-red: #d5203a;
    --band-text: #f6d3ad;
    --rule: #c9b27a;
    --ribbon-top: #d9cc8e;
    --ribbon-bottom: #b6704c;
    --dot-red: #e01e3c;
  }
  * { box-sizing: border-box; margin: 0; padding: 0; }
  html, body { width: 848px; height: 1200px; overflow: hidden; background: var(--ink-bg); }
  .menu {
    position: relative;
    width: 848px; height: 1200px; overflow: hidden;
    background: radial-gradient(ellipse at 50% 55%, var(--ink-bg-glow) 0%, var(--ink-bg) 70%);
    color: var(--gold-text);
    font-family: "Libre Caslon Text", Georgia, serif;
    font-size: 11.1px;
    line-height: 15px;
  }
  .brand {
    position: absolute; left: 0; right: 0; top: 66px;
    display: flex; justify-content: center; align-items: center; gap: 14px;
  }
  .brand-dot { width: 12px; height: 12px; border-radius: 50%; background: var(--dot-red); }
  .brand-name {
    font-family: "Josefin Sans", Arial, sans-serif;
    font-weight: 400; font-size: 50px; letter-spacing: 14px; line-height: 1;
    color: var(--gold-logo);
  }
  .ribbon { position: absolute; left: 701px; top: 0; width: 96px; height: 160px; }

  .section { position: absolute; }
  .band {
    display: inline-block; height: 23px; white-space: nowrap;
    background: var(--band-red); color: var(--band-text);
    font-weight: 700; font-size: 15px; line-height: 25px;
    padding-left: 13px; margin-bottom: 2px;
  }
  .band-note { font-weight: 400; font-size: 11px; }
  .items { list-style: none; padding-left: 14px; }
  .items li { margin-bottom: 4.2px; }
  .nowrap li { white-space: nowrap; }
  .hang li { padding-left: 35px; text-indent: -35px; }
  .cols { display: flex; padding-left: 14px; }
  .cols .items { padding-left: 0; }
  .cols .divided { border-right: 1px solid var(--rule); margin-right: 14px; padding-bottom: 2px; }
  .strong { font-weight: 700; }
  .strong-italic { font-weight: 700; font-style: italic; }
  .light { font-weight: 400; }
</style>
</head>
<body>
<main class="menu">

  <header class="brand">
    <span class="brand-dot"></span>
    <span class="brand-name">HARBOR</span>
  </header>

  <svg class="ribbon" viewBox="0 0 96 160" aria-hidden="true">
    <defs>
      <linearGradient id="ribbonFill" x1="0" y1="0" x2="0" y2="1">
        <stop offset="0" stop-color="#d9cc8e"/>
        <stop offset="1" stop-color="#b6704c"/>
      </linearGradient>
    </defs>
    <path d="M0 0 H96 V160 L48 147 L0 160 Z" fill="url(#ribbonFill)"/>
  </svg>

  <!-- Left column -->
  <section class="section" style="left:42px; top:200px;">
    <h2 class="band" style="width:170px;">SUSHI / SASHIMI</h2>
    <div class="cols">
      <ul class="items divided nowrap" style="width:175px;">
        <li>Toro; blue fin tuna belly (gf)</li>
        <li>Ebi; cooked shrimp (gf)</li>
        <li>Hamachi; yellowtail (gf)</li>
        <li>Uni; sea urchin (gf)</li>
        <li>Hirame; fluke (gf)</li>
      </ul>
      <ul class="items nowrap">
        <li>Unagi; fresh water eel (gf)</li>
        <li>Sake; salmon (gf)</li>
        <li>Madai; red snapper (gf)</li>
        <li>Maguro; tuna (gf)</li>
      </ul>
    </div>
  </section>

  <section class="section" style="left:42px; top:339px; width:352px;">
    <h2 class="band" style="width:170px;">SUSHI PLATTERS</h2>
    <ul class="items hang">
      <li>Small: Five Pieces assorted sushi, nine pieces sashimi, spicy tuna roll (gf)</li>
      <li>Large: Eight Pieces assorted sushi, eighteen pieces of sashimi, alaskan roll, rainbow roll (gf)</li>
    </ul>
  </section>

  <section class="section" style="left:42px; top:450px; width:362px;">
    <h2 class="band" style="width:170px;">CLASSIC ROLLS</h2>
    <ul class="items nowrap">
      <li>Yellowtail; inside out roll with scallions (gf)</li>
      <li>Spicy Tuna or Salmon or Yellowtail; spicy mayo</li>
      <li>California: crab meat, cucumber and avocado (gf)</li>
      <li>Vegetable: avocado, cucumber, asparagus and pickled reddish(gf)</li>
      <li>Spider: soft shell crab and avocado with eel sauce</li>
      <li>Shrimp Tempura: deep fried tempura shrimp and eel sauce</li>
      <li>Alaskan; salmon and avocado (gf)</li>
    </ul>
  </section>

  <section class="section" style="left:42px; top:628px; width:362px;">
    <h2 class="band" style="width:170px;">SPECIAL ROLLS</h2>
    <ul class="items">
      <li>The Harbor: tuna, salmon, yellowtail, avocado, spicy mayo, soy bean paper</li>
      <li>King Crab Rainbow: king crab, avocado, cucumbers, assorted fish on top</li>
      <li>Empress: Shrimp tempura, spicy tuna on top, eel sauce, spicy mayo</li>
      <li>Spicy Girl: Spicy crunchy crab meat, cucumber, shrimp on top</li>
      <li>Dragon: Eel, cucumber, avocado, and tobiko on top, eel sauce</li>
      <li>Yummy: spicy crunchy salmon, avocado, mango and salmon on top</li>
      <li>No. 9: Shrimp Tempura, avocado, kani, spicy mayo, tobiko</li>
      <li>Sunrise Roll: spicy crunchy tuna and avocado, spicy crunchy salmon on top</li>
    </ul>
  </section>

  <section class="section" style="left:42px; top:889px; width:370px;">
    <h2 class="band" style="width:186px;">SEAFOOD RAW BAR</h2>
    <div class="cols">
      <ul class="items divided nowrap" style="width:175px;">
        <li>Lobster Cocktail</li>
        <li>Shrimp Cocktail</li>
        <li>Clams on the Half Shell</li>
      </ul>
      <ul class="items nowrap">
        <li>Oysters on the Half Shell</li>
        <li>Colossal Crab Cocktail</li>
      </ul>
    </div>
    <ul class="items nowrap" style="margin-top:4px;">
      <li class="strong">Raw Bar Plate for One:</li>
      <li>Two Shrimp, Half of a One Pound Lobster,</li>
      <li>Two Clams, One East Coast Oyster, One West Coast Oyster</li>
      <li class="strong">SEAFOOD PLATTERS <span class="light">(gf)</span></li>
      <li>Shrimp, Oysters, Clams, Lobster and Crab</li>
      <li class="strong-italic">Large or Colossal</li>
    </ul>
  </section>

  <section class="section" style="left:163px; top:1116px;">
    <h2 class="band" style="width:122px;">DESSERTS</h2>
    <p style="margin-left:1px; margin-top:2px;">T.B.D. - separate menu</p>
  </section>

  <!-- Right column -->
  <section class="section" style="left:411px; top:200px; width:396px;">
    <h2 class="band" style="width:77px;">APPS</h2>
    <ul class="items">
      <li style="white-space:nowrap;">BAO Bun; hoisin bbq pancetta cut pork loin, &nbsp;crispy onions, micro mint</li>
      <li style="white-space:nowrap;">Five Spice Crispy Popcorn Crusted Prawns (2); classic burre blanc</li>
      <li style="white-space:nowrap;">Jumbo Lump Crab; citrus miso drizzle, spring pea puree, micro greens</li>
      <li>Crispy Wonton Napoleon; &nbsp;cucumber gallete, ahi tuna, jumbo lump crab meat, wasabi aioli, shoestring wontons</li>
      <li>PEI Mussels; charred artichoke hearts, blistered heirloom tomatoes, garlic white wine broth</li>
      <li>New Zealand or Domestic Small Eye Lamb Chop (1); crispy porcini risotto cake</li>
    </ul>
  </section>

  <section class="section" style="left:411px; top:403px; width:396px;">
    <h2 class="band" style="width:95px;">SALADS</h2>
    <ul class="items">
      <li>Classic Wedge; bleu cheese, bacon lardons, heirloom tomatoes</li>
      <li>Mixed Baby Greens; heirloom tomatoes, cucumber, red onion, dijon vinaigrette</li>
      <li>Tabulleh; buckwheat grain, fresh mint, tomato concasse, cucumber, parsley, fresh squeezed lemon, EVOO., salt and pepper</li>
      <li>Tomato Mozzarella Salad / Burratta</li>
      <li>Spinach Salad; green apple, feta, currants, with per-simmons vinaigrette</li>
      <li>Kale Caesar; homemade cacio e'peppe dressing, pecorino and parmesan cheese, toasted croutons.</li>
    </ul>
  </section>

  <section class="section" style="left:411px; top:628px; width:396px;">
    <h2 class="band" style="width:106px;">ENTREES</h2>
    <ul class="items">
      <li>Pan Roasted Miso Glazed Black Cod; green tea noodle stir fry; Napa cabbage, carrot, Japanese eggplant</li>
      <li>Pan Seared Striped Bass; lobster succotash in a tomato saffron broth</li>
      <li>E.V.O.O. Salted / Grilled Swordfish; sun dried tomato, olive and caper tapenade, over basmati rice</li>
      <li>Grilled Half Chicken; sun dried tomato and basil Israeli cous-cous, pan au jus</li>
      <li>Roasted Fresh Caviatelle Ratatoille; vegetable broth</li>
      <li>Lobster Cartoccio; shrimp, mussels, clams, fresh herb tomato broth, tossed with bucatini</li>
      <li>Charred Artichoke Hearts, heirloom tomatoes, caper berries, spring onions, fresh basil, white wine reduction over forbidden rice (gf)</li>
      <li>Mediterranean Grilled Veggie Plate; artichoke hearts, Japanese eggplant, green &amp; white asparagus, seared heirloom tomatoes, roasted baby carrots, cauliflower rice, evoo &amp; fig drizzle (gf)</li>
    </ul>
  </section>

  <section class="section" style="left:411px; top:928px;">
    <h2 class="band" style="padding-right:4px; font-size:14.4px;">USDA PRIME STEAKS <span class="band-note">(gf)</span></h2>
    <ul class="items nowrap" style="padding-left:12px;">
      <li>10 Oz Filet</li>
      <li>14 or 16 oz New York Strip</li>
      <li>24 oz Boneless Ribeye</li>
      <li>36 oz Bone in Rib Eye</li>
      <li>Berkshire Pork Chop</li>
    </ul>
  </section>

  <section class="section" style="left:619px; top:928px;">
    <h2 class="band" style="width:79px; padding-left:8px;">SAUCES</h2>
    <ul class="items nowrap" style="padding-left:7px;">
      <li>Cabernet Demi Glaz</li>
      <li>Gorganzola Brulle Cream</li>
      <li>Truffled Wild Mushroom Ragu</li>
      <li>Horseradish Cream</li>
      <li>House Steak Sauce</li>
    </ul>
  </section>

  <section class="section" style="left:411px; top:1053px; width:400px;">
    <h2 class="band" style="width:75px;">SIDES</h2>
    <ul class="items nowrap">
      <li>Bacon, Sweet Corn, Caramelized Vidalia Onion fingerling potatoes</li>
    </ul>
    <div class="cols">
      <ul class="items nowrap" style="width:155px;">
        <li>Mashed Idaho Potatoes</li>
        <li>Roasted Peanut Potatoes</li>
        <li>Creamed Spinach</li>
        <li>Sautéed Spinach</li>
      </ul>
      <ul class="items nowrap" style="width:134px;">
        <li>Grilled Asparagus</li>
        <li>French Beans</li>
        <li>Israeli Cous Cous</li>
        <li>Sweet Potato Steak Fries</li>
      </ul>
      <ul class="items nowrap">
        <li>Corn Skillet</li>
      </ul>
    </div>
  </section>

</main>
</body>
</html>
```